Marisa Dee Creations & Affairs business card

I need an elegant informative but not busy business card using my logo. We are a florist with high end customers. I am adding a PDF file and a PNG file for those who requested it

Reason: still working on changes

Reason: Working on changes

Reason: making changes

Target Market(s)

Brides, grooms, men purchasing flowers
Ages 20-65

Industry/Entity Type

Florist

Requirements
Must have
• Business info:
Marisa Dee Creation & Affairs
www.marisadeeaffairs.example.
555-418-7362

555-418-7362
Nice to have
• Est 1954
may want Pinterest logo, twitter and linkedin and facbook
Should not have
• Clip art or photos

```html
<!DOCTYPE html>
<html lang="en">
<head>
<meta charset="utf-8">
<title>Marisa Dee Creations &amp; Affairs – Business Card</title>
<link href="https://fonts.googleapis.com/css2?family=Cinzel:wght@400&family=Open+Sans:wght@400;600&display=swap" rel="stylesheet">
<style>
  :root {
    --backdrop: #ece9e4;
    --card: #fbfbfa;
    --frame: #464646;
    --ink: #2b2b2b;
    --ink-soft: #3c3c3c;
    --blush: #efaec0;
  }
  * { box-sizing: border-box; margin: 0; padding: 0; }
  html, body {
    width: 1200px;
    height: 750px;
    overflow: hidden;
    background: var(--backdrop);
  }
  .stage {
    position: relative;
    width: 1200px;
    height: 750px;
    display: flex;
    align-items: center;
    justify-content: center;
    gap: 50px;
  }
  .card {
    position: relative;
    width: 520px;
    height: 298px;
    background: var(--card);
    box-shadow: 0 6px 18px rgba(0,0,0,0.12);
  }
  .card-frame {
    position: absolute;
    inset: 16px;
    border: 6px solid var(--frame);
  }

  /* Front face */
  .front-content {
    position: absolute;
    inset: 0;
    display: flex;
    flex-direction: column;
    align-items: center;
    justify-content: center;
    text-align: center;
  }
  .brand-mark {
    width: 50px;
    height: 50px;
    margin-bottom: 10px;
  }
  .front-name,
  .front-name-sub {
    font-family: "Cinzel", serif;
    font-weight: 400;
    color: var(--ink);
  }
  .front-name {
    font-size: 32px;
    letter-spacing: 4px;
    line-height: 1;
  }
  .front-name-sub {
    font-size: 11px;
    letter-spacing: 3.5px;
    margin-top: 6px;
  }
  .front-web {
    font-family: "Open Sans", sans-serif;
    font-size: 11px;
    color: var(--ink-soft);
    margin-top: 7px;
  }

  /* Back face */
  .back-content {
    position: absolute;
    inset: 0;
    display: flex;
    align-items: center;
    padding-left: 52px;
    gap: 22px;
  }
  .back-mark {
    width: 72px;
    height: 72px;
    flex: none;
  }
  .back-heading {
    font-family: "Open Sans", sans-serif;
    font-weight: 400;
    font-size: 17px;
    color: var(--ink);
    letter-spacing: 0.2px;
    margin-bottom: 6px;
  }
  .contact-list {
    list-style: none;
    font-family: "Open Sans", sans-serif;
    font-size: 11.5px;
    line-height: 1.45;
    color: var(--ink-soft);
  }
  .contact-label { font-weight: 600; }
</style>
</head>
<body>
  <main class="stage">
    <section class="card card-front" aria-label="Business card front">
      <div class="card-frame"></div>
      <div class="front-content">
        <svg class="brand-mark" viewBox="0 0 50 50" aria-hidden="true">
          <circle cx="25" cy="25" r="22" fill="none" stroke="var(--blush)" stroke-width="2"/>
        </svg>
        <h1 class="front-name">Marisa Dee</h1>
        <p class="front-name-sub">Creations &amp; Affairs</p>
        <p class="front-web">www.marisadeeaffairs.example</p>
      </div>
    </section>

    <section class="card card-back" aria-label="Business card back">
      <div class="card-frame"></div>
      <div class="back-content">
        <svg class="back-mark" viewBox="0 0 72 72" aria-hidden="true">
          <circle cx="36" cy="36" r="32" fill="none" stroke="var(--blush)" stroke-width="2"/>
        </svg>
        <div class="back-details">
          <h2 class="back-heading">MARISA DEE CREATION &amp; AFFAIRS</h2>
          <ul class="contact-list">
            <li class="contact-address">218 W Elm Avenue, Brookhaven, OH 43210</li>
            <li><span class="contact-label">tel:</span> 555-418-7362</li>
            <li><span class="contact-label">email:</span> marisadee@mail.example</li>
            <li><span class="contact-label">web:</span> www.marisadeeaffairs.example</li>
          </ul>
        </div>
      </div>
    </section>
  </main>
</body>
</html>
```